jot school poster design and change logo name

We already have a logo which only needs to be slightly modified with "school".
We also have two advertising faces, a girl and a boy, which should be on our poster.
Important key data:

bilingual D/E small classes
daycare
private kindergarten
private school from 2024

Poster size: 268,5 x 128 cm
We need logo sizes in different sizes
also for T-shirts.
Attached also a old poster

new clients

0094D4
00A9DD
6FCCEA
C7EBF8
E9F6FB
59FF00
82FF00
B8FF75
E3FFCB
F4FFEA
FFC000
F8CF3A
FAE287
FDF2CF
FEFAEE
F0912C
F2A743
F7CA91
FBE8D2
FDF5EE

```html
<!DOCTYPE html>
<html lang="de">
<head>
<meta charset="utf-8">
<title>jot school – Banner</title>
<link href="https://fonts.googleapis.com/css2?family=Fredoka:wght@600;700&family=Montserrat:wght@500&family=Poppins:wght@600;700&display=swap" rel="stylesheet">
<style>
  :root{
    --sky:#00A9DD;
    --sky-deep:#0094D4;
    --sky-light:#6FCCEA;
    --orange:#FFC000;
    --orange-deep:#F8A01C;
    --school-text:#FDF2CF;
    --pink:#DE2F8A;
    --lime:#C9E500;
    --ink:#1a1a1a;
    --white:#ffffff;
    --stage:#ececec;
  }
  *{margin:0;padding:0;box-sizing:border-box}
  html,body{width:1200px;height:912px;overflow:hidden;background:var(--stage)}
  .banner{
    position:absolute;left:0;top:170px;width:1200px;height:571px;overflow:hidden;
    background:radial-gradient(circle at 40% 30%, var(--sky-light) 0%, var(--sky) 45%, var(--sky-deep) 100%);
  }
  .headline{position:absolute;left:50px;font-family:"Fredoka",sans-serif;font-weight:700;line-height:1;letter-spacing:-0.5px;white-space:nowrap}
  .headline--top{top:38px;color:var(--orange);font-size:60px}
  .headline--main{top:98px;color:var(--white);font-size:84px}
  .age-box{position:absolute;left:45px;top:194px;width:576px;height:82px;background:var(--pink);border-radius:22px;overflow:hidden}
  .age-box__from{position:absolute;left:23px;top:8px;font-family:"Montserrat",sans-serif;font-weight:500;font-size:26px;color:var(--white);white-space:nowrap}
  .age-box__until{position:absolute;left:57px;top:45px;width:463px;height:40px;background:var(--lime);border-radius:40px 40px 0 0;
    font-family:"Montserrat",sans-serif;font-weight:500;font-size:29px;color:var(--ink);text-align:center;line-height:38px}
  .offer{position:absolute;top:292px;height:48px;font-family:"Poppins",sans-serif;font-weight:700;font-size:23px;line-height:44px;white-space:nowrap}
  .offer--school{left:310px;width:316px;background:var(--orange-deep);color:var(--school-text);border-radius:0 24px 24px 0;padding-left:34px}
  .offer--kindergarten{left:45px;width:285px;border:2px solid var(--white);background:var(--sky);color:var(--white);border-radius:0 24px 24px 0;padding-left:10px}
  .pitch{position:absolute;left:45px;top:351px;font-family:"Poppins",sans-serif;font-weight:700;font-size:22px;line-height:27px;color:var(--white);white-space:nowrap}
  .footer{position:absolute;left:0;top:421px;width:1200px;height:150px;background:var(--white)}
  .brand{position:absolute;left:39px;top:28px;width:134px;display:flex;flex-direction:column;align-items:center;gap:8px}
  .brand__dot{width:44px;height:44px;border-radius:50%;background:var(--orange)}
  .brand__name{font-family:"Fredoka",sans-serif;font-weight:700;font-size:29px;line-height:1;color:var(--orange-deep);white-space:nowrap}
  .contact{position:absolute;left:197px;font-family:"Poppins",sans-serif;font-weight:700;color:var(--ink);display:flex;align-items:center;gap:10px;white-space:nowrap;line-height:1.2}
  .contact svg{width:18px;height:18px;flex:none}
  .contact--phone{top:24px;font-size:27px}
  .contact--address{top:68px;font-size:20px;font-weight:600}
  .contact--web{top:92px;font-size:32px}
  .sun{position:absolute;left:860px;top:55px;width:440px;height:440px;border-radius:50%;background:var(--orange-deep)}
  .photo{position:absolute;inset:0}
  .photo__boy{position:absolute;left:900px;top:125px;width:420px;height:470px;border-radius:50%;
    background:linear-gradient(135deg,#f1c6a6 0%,var(--pink) 45%,#2aa8e0 100%);box-shadow:0 0 0 9px var(--white)}
  .photo__girl{position:absolute;left:600px;top:265px;width:360px;height:320px;border-radius:180px 180px 0 0;
    background:linear-gradient(180deg,#9c6a45 0%,#f0c2a0 40%,#f6d6c2 100%)}
  .overlay{position:absolute;left:0;top:0;width:1200px;height:571px}
</style>
</head>
<body>
  <section class="banner">
    <h1 class="headline headline--top">ZWEISPRACHIGE D/E</h1>
    <h2 class="headline headline--main">KLEINKLASSEN</h2>

    <div class="age-box">
      <p class="age-box__from">Kinderkrippe &amp; Hort&nbsp; Ab 3.Lebensmonat</p>
      <p class="age-box__until">bis zum 12. Lebensjahr</p>
    </div>

    <div class="offer offer--school">Privatschule ab 2024</div>
    <div class="offer offer--kindergarten">Privater Kindergarten</div>

    <p class="pitch">Bei uns lernen ALLE Kinder spielend einfach in<br>kirzester Zeit Englisch wie eine 2. Muttersprache.</p>

    <div class="footer">
      <div class="brand"><span class="brand__dot"></span><span class="brand__name">jot school</span></div>
      <p class="contact contact--phone">
        <svg viewBox="0 0 24 24"><path fill="#DE2F8A" d="M6.6 10.8a15 15 0 0 0 6.6 6.6l2.2-2.2c.3-.3.7-.4 1-.2 1.1.4 2.3.6 3.6.6.6 0 1 .4 1 1V20c0 .6-.4 1-1 1A17 17 0 0 1 3 4c0-.6.4-1 1-1h3.5c.6 0 1 .4 1 1 0 1.3.2 2.5.6 3.6.1.3 0 .7-.2 1z"/></svg>
        +41 79 555 01 23</p>
      <p class="contact contact--address">
        <svg viewBox="0 0 24 24"><path fill="#DE2F8A" d="M12 2a7 7 0 0 0-7 7c0 5.2 7 13 7 13s7-7.8 7-13a7 7 0 0 0-7-7zm0 9.5A2.5 2.5 0 1 1 12 6.5a2.5 2.5 0 0 1 0 5z"/></svg>
        Lindenweg 12, 8000 Musterdorf</p>
      <p class="contact contact--web">
        <svg viewBox="0 0 24 24"><circle cx="12" cy="12" r="9" fill="none" stroke="#DE2F8A" stroke-width="2"/><path d="M3 12h18M12 3c3 3 3 15 0 18M12 3c-3 3-3 15 0 18" fill="none" stroke="#DE2F8A" stroke-width="2"/></svg>
        www.jot-daycare.ch</p>
    </div>

    <div class="sun"></div>
    <div class="photo" role="img" aria-label="Foto: lachendes Mädchen und Junge mit bunt bemalten Händen vor pinkem Hintergrund">
      <div class="photo__boy"></div>
      <div class="photo__girl"></div>
    </div>

    <svg class="overlay" viewBox="0 0 1200 571">
      <defs><path id="daycare-arc" d="M690.7 162.6 A112 112 0 0 1 857 85"/></defs>
      <text font-family="Fredoka, sans-serif" font-weight="700" font-size="40" fill="#fff" letter-spacing="2">
        <textPath href="#daycare-arc">DAYCARE</textPath>
      </text>
      <g transform="translate(630.5 4.9) scale(1.1)">
        <polygon fill="#C9E500" points="155,72 166,96 187,80 190,106 215,98 209,123 235,124 221,146 245,157 224,172 241,191 216,196 225,221 200,216 199,242 178,228 166,250 155,226 144,250 132,228 111,242 110,216 85,221 94,196 69,191 86,172 65,157 89,146 75,124 101,123 95,98 120,106 123,80 144,96"/>
        <text x="155" y="141" text-anchor="middle" font-family="Fredoka, sans-serif" font-weight="700" font-size="18" fill="#1a1a1a">DO YOU</text>
        <text x="155" y="170" text-anchor="middle" font-family="Fredoka, sans-serif" font-weight="700" font-size="29" fill="#1a1a1a">SPEAK</text>
        <text x="155" y="193" text-anchor="middle" font-family="Fredoka, sans-serif" font-weight="700" font-size="20" fill="#1a1a1a">ENGLISH?</text>
      </g>
    </svg>
  </section>
</body>
</html>
```